Beekeeper needs a label for honey jars

Ciao! I'm from Como Italy
I'm a hobbyist beekeeper and I produce honey for myself and my friends.
I've named my apiary "Dado di sole," a play on words between my nickname (Dado, from Edoardo) and the Italian expression "Dado di sole," which translates to "a drizzle of honey" in English.
I need to create a label for my honey glass jars (250 gr and 500 gr).
I don't need a label for commercial purposes. I would like to include at least the name “Apicoltura Dado di sole", the type of honey (e.g., wildflower, acacia...) and a space for the production year, to be handwritten each year.
In the design some references to the world of bees.
For reference, attached a label with a style I like
Attached are the images of the selected jars and their measurements
Thanks and good job!

beekeeping, honey

• I would like an elegant style with clean graphics.
• Predominance of black color.

```html
<!DOCTYPE html>
<html lang="it">
<head>
<meta charset="utf-8">
<title>Apicoltura Dado di sole – Honey labels</title>
<link href="https://fonts.googleapis.com/css2?family=Barlow:wght@300;400&family=Mrs+Saint+Delafield&display=swap" rel="stylesheet">
<style>
  :root {
    --board: #cccccc;
    --ink: #000000;
    --paper: #ffffff;
    --gold: #c8922d;
    --gold-soft: #3a2a0c;
    --grey-soft: #e6e6e6;
  }
  html, body {
    margin: 0;
    width: 1200px;
    height: 693px;
    overflow: hidden;
    background: var(--board);
  }
  .board {
    position: relative;
    width: 1200px;
    height: 693px;
  }
  .label {
    position: absolute;
    top: 116px;
    width: 440px;
    height: 451px;
    overflow: hidden;
    font-family: "Barlow", "Helvetica Neue", Arial, sans-serif;
    font-weight: 300;
  }
  .label p, .label h1 { margin: 0; }
  .label--dark  { left: 119px; background: var(--ink); color: var(--paper); }
  .label--light { left: 655px; background: var(--paper); color: var(--ink); }

  .claim-row {
    position: absolute;
    top: 38px;
    left: 0;
    width: 100%;
    display: flex;
    align-items: center;
    justify-content: center;
    gap: 4px;
  }
  .claim {
    font-size: 17px;
    line-height: 1;
    letter-spacing: 0.3em;
    padding-left: 0.3em;
    white-space: nowrap;
  }
  .claim-rule {
    flex: 1;
    height: 3px;
    background: var(--ink);
    margin-top: 3px;
  }

  .bee-mark {
    position: absolute;
    left: 162px;
    top: 68px;
    width: 116px;
    height: 93px;
    border-radius: 46px;
  }
  .label--dark .bee-mark  { background: radial-gradient(circle, #5a4116 0%, #1c1408 70%, transparent 100%); }
  .label--light .bee-mark { background: radial-gradient(circle, #bdbdbd 0%, #efefef 70%, transparent 100%); }

  .product {
    position: absolute;
    top: 168px;
    left: 0;
    width: 100%;
    text-align: center;
    font-size: 46px;
    line-height: 1;
    letter-spacing: 0.5em;
    padding-left: 0.5em;
    box-sizing: border-box;
    font-weight: 400;
  }

  .comb-band {
    position: absolute;
    left: 0;
    top: 235px;
    width: 100%;
    height: 140px;
  }
  .label--dark .comb-band  { background: linear-gradient(180deg, #000 0%, var(--gold-soft) 50%, #000 100%); }
  .label--light .comb-band { background: linear-gradient(180deg, #fff 0%, var(--grey-soft) 50%, #fff 100%); }

  .apiary {
    position: absolute;
    left: 203px;
    top: 254px;
    font-size: 19px;
    line-height: 1;
    letter-spacing: 0.2em;
    z-index: 2;
  }
  .apiary-name {
    position: absolute;
    left: 60px;
    top: 266px;
    width: 320px;
    text-align: center;
    font-family: "Mrs Saint Delafield", cursive;
    font-size: 74px;
    line-height: 1;
    font-weight: 400;
    z-index: 2;
  }

  .year-field {
    position: absolute;
    left: 110px;
    top: 400px;
    width: 220px;
    height: 28px;
  }
  .year-field svg { position: absolute; inset: 0; }
  .year-field span {
    position: absolute;
    left: 12px;
    top: 7px;
    font-size: 13px;
    line-height: 1;
    font-weight: 400;
  }
  .label--dark .year-field span { color: var(--ink); }
  .year-field--caps span { text-transform: uppercase; }
</style>
</head>
<body>
<main class="board">

  <section class="label label--dark">
    <div class="claim-row"><p class="claim">100% NATURAL</p></div>
    <div class="bee-mark" role="img" aria-label="Line-art bee emblem in gold"></div>
    <h1 class="product">HONEY</h1>
    <div class="comb-band" role="img" aria-label="Gold honeycomb line pattern"></div>
    <p class="apiary">APICOLTURA</p>
    <p class="apiary-name">Dado di sole</p>
    <div class="year-field">
      <svg width="220" height="28" viewBox="0 0 220 28" aria-hidden="true">
        <path d="M5 0 H215 A5 5 0 0 0 220 5 V23 A5 5 0 0 0 215 28 H5 A5 5 0 0 0 0 23 V5 A5 5 0 0 0 5 0 Z" fill="var(--paper)"/>
      </svg>
      <span>Production Year</span>
    </div>
  </section>

  <section class="label label--light">
    <div class="claim-row">
      <div class="claim-rule"></div>
      <p class="claim">100% NATURAL</p>
      <div class="claim-rule"></div>
    </div>
    <div class="bee-mark" role="img" aria-label="Line-art bee emblem in black"></div>
    <h1 class="product">HONEY</h1>
    <div class="comb-band" role="img" aria-label="Black honeycomb line pattern with two filled cells"></div>
    <p class="apiary">APICOLTURA</p>
    <p class="apiary-name">Dado di sole</p>
    <div class="year-field year-field--caps">
      <svg width="220" height="28" viewBox="0 0 220 28" aria-hidden="true">
        <path d="M5 0.5 H215 A4.5 4.5 0 0 0 219.5 5 V23 A4.5 4.5 0 0 0 215 27.5 H5 A4.5 4.5 0 0 0 0.5 23 V5 A4.5 4.5 0 0 0 5 0.5 Z" fill="none" stroke="var(--ink)" stroke-width="1"/>
      </svg>
      <span>Production Year</span>
    </div>
  </section>

</main>
</body>
</html>
```